dkfarrowplace website

I need a new homepage design for my current website at www.DKFarrowPlace.example. I want someone to look at my current website and develop a more appealing homepage... right now the colors don't blend very well and it needs a facelift

Reason: This has been extended to September 10th

```html
<!DOCTYPE html>
<html lang="en">
<head>
<meta charset="utf-8">
<title>D K Farrow – Home</title>
<link href="https://fonts.googleapis.com/css2?family=Roboto:wght@400;500;700&display=swap" rel="stylesheet">
<style>
:root{
  --pink:#e22f8c;
  --rose:#e0245a;
  --pink-line:#f0a8cc;
  --grey-bg:#ececec;
  --hero-grey:#7a7a7a;
  --text:#222;
  --muted:#777;
  --panel:#f3f3f3;
  --white:#fff;
  --border:#cfcfcf;
}
*{box-sizing:border-box;margin:0;padding:0}
html,body{width:1200px;height:1000px;overflow:hidden}
body{background:var(--grey-bg);font-family:'Roboto',Arial,sans-serif;color:var(--text);position:relative}
.page{position:absolute;left:179px;top:0;width:893px;height:1000px;background:var(--white);box-shadow:0 0 18px rgba(0,0,0,.25)}
.topbar{position:absolute;left:0;top:0;width:893px;height:7px;background:var(--pink)}
.nav{position:absolute;left:106px;top:7px;height:68px;display:flex}
.brand{width:123px;height:68px;background:var(--pink);color:var(--white);font-size:22px;font-weight:400;display:flex;align-items:center;justify-content:center;letter-spacing:.5px}
.nav-item{width:81px;height:68px;border-right:1px solid var(--pink-line);color:var(--pink);font-size:14px;display:flex;align-items:center;justify-content:center;text-align:center;line-height:16px;position:relative}
.nav-item.active{background:var(--pink);color:var(--white)}
.nav-item.active::after{content:"";position:absolute;bottom:0;left:36px;border:5px solid transparent;border-bottom-color:var(--white)}
.hero-band{position:absolute;left:0;top:75px;width:893px;height:223px;background:linear-gradient(#5c5c5c,#8a8a8a 30%,#7d7d7d)}
.hero{position:absolute;left:110px;top:8px;width:680px;height:215px;background:var(--white);padding:4px 4px 0}
.hero-img{width:100%;height:100%;background:linear-gradient(90deg,#9aa6b4 0%,#b9c3cc 40%,#8f99a3 65%,#3d3b40 85%,#222 100%)}
.hero-copy{position:absolute;left:105px;top:70px;width:270px;text-align:center;color:var(--white)}
.hero-copy h1{font-size:26px;font-weight:700}
.hero-copy p{font-size:13px;font-weight:500;margin-top:12px;padding-bottom:10px;border-bottom:1px solid var(--white)}
.hero-btn{display:inline-block;margin-top:12px;border:2px solid var(--white);font-size:10px;font-weight:700;padding:4px 14px}
.hero-arrow{position:absolute;top:99px;width:18px;height:18px}
.optin{position:absolute;left:106px;top:298px;width:681px;height:80px;border-bottom:2px solid var(--pink)}
.optin-cover{position:absolute;left:12px;top:7px;width:50px;height:66px;background:linear-gradient(135deg,#f6f6f6,#d8d8e6);border-right:4px solid #3558a8}
.optin-text{position:absolute;left:74px;top:16px;width:210px;font-size:8.5px;line-height:13px}
.optin-text h3{color:var(--pink);font-size:10px;font-weight:500;margin-bottom:3px}
.optin-divider{position:absolute;left:278px;top:6px;width:1px;height:70px;background:#ddd}
.field{position:absolute;top:13px;height:26px;background:#ececec;border:1px solid #ddd;font-size:10px;color:#999;padding-left:32px;line-height:24px}
.field-icon{position:absolute;left:-1px;top:-1px;width:26px;height:26px;background:var(--pink)}
.subscribe{position:absolute;left:585px;top:13px;width:84px;height:26px;background:var(--rose);color:var(--white);font-size:10px;font-weight:700;text-align:center;line-height:26px}
.privacy{position:absolute;left:286px;top:47px;width:390px;font-size:8.5px;line-height:13px}
.privacy b{color:var(--rose);font-weight:400}
.products{position:absolute;left:117px;top:402px;display:flex;gap:15px}
.card{width:153px;height:256px;border:1.5px solid var(--border);border-radius:8px;text-align:center;position:relative}
.card-cover{position:absolute;left:38px;top:10px;width:72px;height:118px;border-radius:2px}
.card-rule{position:absolute;left:20px;top:140px;width:113px;height:1px;background:#ddd}
.card p{position:absolute;left:8px;top:152px;width:137px;font-size:8.5px;line-height:13px}
.more{position:absolute;left:45px;top:225px;width:67px;height:15px;background:var(--rose);border-radius:8px;color:var(--white);font-size:9.5px;line-height:15px;text-align:left;padding-left:13px}
.more svg{position:absolute;right:0;top:0}
.section-head{position:absolute;left:106px;width:681px;height:26px;background:var(--panel);border-left:3px solid var(--pink);color:var(--pink);font-size:11.5px;font-weight:500;line-height:26px;padding-left:7px}
.section-head svg{position:absolute;right:12px;top:7px}
.testimonials{position:absolute;left:106px;top:716px;width:681px;display:flex;justify-content:space-between;padding:0 10px}
.quote{width:150px;text-align:center;font-size:8.5px;line-height:13px;color:var(--muted)}
.quote b{display:block;color:var(--muted);font-weight:500}
.press{position:absolute;left:109px;top:863px;display:flex;gap:14px}
.press-box{width:124px;height:75px;border:1px solid var(--border);display:flex;align-items:center;justify-content:center}
.footer{position:absolute;left:0;top:954px;width:893px;height:46px;background:var(--rose)}
.footer p{position:absolute;left:113px;top:22px;font-size:8.5px;color:var(--white)}
.social{position:absolute;top:10px;width:28px;height:28px;border-radius:50%;background:#d81e50;box-shadow:0 0 0 2px #e85a80 inset}
</style>
</head>
<body>
<div class="page">
  <div class="topbar"></div>
  <nav class="nav">
    <div class="brand">D K Farrow</div>
    <div class="nav-item">Home</div>
    <div class="nav-item">Products</div>
    <div class="nav-item active">About</div>
    <div class="nav-item">Blog</div>
    <div class="nav-item">Forum</div>
    <div class="nav-item">Media<br>Room</div>
    <div class="nav-item">Success<br>Stories</div>
  </nav>

  <section class="hero-band">
    <div class="hero">
      <div class="hero-img" role="img" aria-label="Photo of a woman with long dark hair and a colourful earring against a blurred beach"></div>
      <div class="hero-copy">
        <h1>DISCOVER</h1>
        <p>Secrets to a Slimmer Sexier and Healthier you!</p>
        <span class="hero-btn">Read More</span>
      </div>
      <svg class="hero-arrow" style="left:20px" viewBox="0 0 18 18"><circle cx="9" cy="9" r="9" fill="#333"/><path d="M10.5 5 6.5 9l4 4" stroke="#fff" stroke-width="1.6" fill="none"/></svg>
      <svg class="hero-arrow" style="left:647px" viewBox="0 0 18 18"><path d="M7.5 5l4 4-4 4" stroke="#ddd" stroke-width="1.4" fill="none"/></svg>
    </div>
  </section>

  <section class="optin">
    <div class="optin-cover" role="img" aria-label="Free report cover"></div>
    <div class="optin-text">
      <h3>5 Reasons You ca't Lose Weight"</h3>
      Just enter your name and email below to get instant access to this 30 page report absolutely FREE!
    </div>
    <div class="optin-divider"></div>
    <div class="field" style="left:286px;width:144px"><span class="field-icon"><svg width="26" height="26"><circle cx="13" cy="10" r="3.5" fill="#fff"/><path d="M7 20a6 6 0 0 1 12 0z" fill="#fff"/></svg></span>Your Name</div>
    <div class="field" style="left:435px;width:145px"><span class="field-icon"><svg width="26" height="26"><rect x="6" y="8" width="14" height="10" fill="#fff"/><path d="M6 8l7 6 7-6" stroke="#e22f8c" stroke-width="1.2" fill="none"/></svg></span>Your E-mail</div>
    <div class="subscribe">SUBSCRIBE</div>
    <p class="privacy"><b>E-mail Privacy</b>: Sign up with complete confidence! We will never sell, rent, lease, or Share your information with anyone.</p>
  </section>

  <section class="products">
    <div class="card"><div class="card-cover" role="img" aria-label="Pink weight loss book cover" style="background:linear-gradient(135deg,#f7c6e0,#e4489a)"></div><div class="card-rule"></div><p>The 12-Day Fresh Greens Reset will jump-start your weight loss, increase your energy level, clear your mind, and improve your overall health....</p><span class="more">More<svg width="22" height="15"><rect width="22" height="15" rx="7" fill="#c81c4c"/><path d="M8 4l6 3.5-6 3.5z" fill="#fff"/></svg></span></div>
    <div class="card"><div class="card-cover" role="img" aria-label="Green smoothie book cover" style="background:linear-gradient(#e9f3f6,#7fb86a)"></div><div class="card-rule"></div><p>The 12-Day Fresh Greens Reset will jump-start your weight loss, increase your energy level, clear your mind, and improve your overall health....</p><span class="more">More<svg width="22" height="15"><rect width="22" height="15" rx="7" fill="#c81c4c"/><path d="M8 4l6 3.5-6 3.5z" fill="#fff"/></svg></span></div>
    <div class="card"><div class="card-cover" role="img" aria-label="Foods chart book cover" style="background:linear-gradient(135deg,#fbe4f0,#e88ab8)"></div><div class="card-rule"></div><p>The 12-Day Fresh Greens Reset will jump-start your weight loss, increase your energy level, clear your mind, and improve your overall health....</p><span class="more">More<svg width="22" height="15"><rect width="22" height="15" rx="7" fill="#c81c4c"/><path d="M8 4l6 3.5-6 3.5z" fill="#fff"/></svg></span></div>
    <div class="card"><div class="card-cover" role="img" aria-label="Belly fat book cover" style="background:linear-gradient(135deg,#f4f4f4,#e4457c)"></div><div class="card-rule"></div><p>The 12-Day Fresh Greens Reset will jump-start your weight loss, increase your energy level, clear your mind, and improve your overall health....</p><span class="more">More<svg width="22" height="15"><rect width="22" height="15" rx="7" fill="#c81c4c"/><path d="M8 4l6 3.5-6 3.5z" fill="#fff"/></svg></span></div>
  </section>

  <h2 class="section-head" style="top:681px">Testimonial<svg width="26" height="12"><path d="M10 0v12L0 6z" fill="#e22f8c"/><path d="M16 0v12l10-6z" fill="#e22f8c"/></svg></h2>
  <section class="testimonials">
    <p class="quote">Lorem ipsum dolor sit amet, consectetur adipiscing elit. Sed cursus non ipsum eu volutpat. Quisque feugiat magna metus, sit amet porta turpis scelerisque eu. Suspendisse facilisis posuere pharetra. Quisque molestie arcu massa,<b>Tomas Reyes, CEO</b></p>
    <p class="quote">Lorem ipsum dolor sit amet, consectetur adipiscing elit. Sed cursus non ipsum eu volutpat. Quisque feugiat magna metus, sit amet porta turpis scelerisque eu. Suspendisse facilisis posuere pharetra. Quisque molestie arcu massa,<b>Tomas Reyes, CEO</b></p>
    <p class="quote">Lorem ipsum dolor sit amet, consectetur adipiscing elit. Sed cursus non ipsum eu volutpat. Quisque feugiat magna metus, sit amet porta turpis scelerisque eu. Suspendisse facilisis posuere pharetra. Quisque molestie arcu massa,<b>Tomas Reyes, CEO</b></p>
  </section>

  <h2 class="section-head" style="top:824px">As See on<svg width="26" height="12"><path d="M10 0v12L0 6z" fill="#e22f8c"/><path d="M16 0v12l10-6z" fill="#e22f8c"/></svg></h2>
  <section class="press">
    <div class="press-box"><svg width="70" height="26"><rect width="70" height="26" rx="3" fill="#d6d6d6"/></svg></div>
    <div class="press-box"><svg width="90" height="22"><rect width="90" height="22" rx="11" fill="#d6d6d6"/></svg></div>
    <div class="press-box"><svg width="94" height="20"><rect width="94" height="20" fill="#d6d6d6"/></svg></div>
    <div class="press-box"><svg width="40" height="40"><circle cx="20" cy="20" r="18" fill="#d6d6d6"/></svg></div>
    <div class="press-box"><svg width="34" height="34"><rect width="34" height="34" rx="4" fill="#d6d6d6"/></svg></div>
  </section>

  <footer class="footer">
    <p>Privacy Policy | Terms of Use | Disclaimer | Copyright © 2014 Marlow Lane Publishing</p>
    <span class="social" style="left:711px"></span>
    <span class="social" style="left:749px"></span>
  </footer>
</div>
</body>
</html>
```